Doctors clinic requires stationary designed

We require various types of stationary to be design based on the logo (attached). We require the following:
- Letterhead (A4 Portrait)
- Business Card (must include UV spot on rear)
- With compliments slip (DL Landscape)
- Appointments card (Folded A6)

We are a young clinical practice which boasts a modern and sophisticated approach to medicine so we require something which feels fresh and modern. Please include colours represented in the logo (contrasting teal and grey). We are calling for creative minds to put forth their ideas and we will be actively providing feedback on all designs.

thank you

Clinic

```html
<!DOCTYPE html>
<html lang="en">
<head>
<meta charset="utf-8">
<title>Dr Clara Westwood – Stationery Suite</title>
<link rel="stylesheet" href="https://fonts.googleapis.com/css2?family=Source+Sans+3:wght@400;600&display=swap">
<style>
  :root {
    --teal: #0f9a87;
    --teal-light: #7fcfc3;
    --grey: #a9abae;
    --grey-soft: #e6e7e8;
    --paper: #ffffff;
    --backdrop: #124c47;
    --font: "Source Sans 3", sans-serif;
  }
  * { box-sizing: border-box; margin: 0; padding: 0; }
  html, body { width: 1200px; height: 900px; overflow: hidden; }
  body { background: var(--backdrop); font-family: var(--font); position: relative; }

  .sheet { position: absolute; background: var(--paper); overflow: hidden; }

  .brand { display: flex; align-items: center; gap: 10px; }
  .brand__mark { width: 30px; height: 30px; border-radius: 50%; border: 3px solid var(--teal); flex: none; }
  .brand__name { color: var(--teal); font-weight: 600; font-size: 22px; letter-spacing: -0.3px; white-space: nowrap; }
  .tagline { color: var(--teal); font-weight: 600; font-size: 12px; white-space: nowrap; }
  .tagline .and { color: var(--grey); font-weight: 400; }

  .contact { font-size: 9px; line-height: 1.3; color: var(--grey); }

  /* Letterhead */
  .letterhead { left: 40px; top: 50px; width: 560px; height: 792px; }
  .letterhead__header { position: absolute; left: 48px; top: 56px; display: flex; align-items: center; gap: 12px; }
  .letterhead__divider { width: 1px; height: 30px; background: var(--grey); }
  .letterhead__contact { position: absolute; left: 88px; top: 112px; display: flex; gap: 40px; }
  .letterhead__pattern { position: absolute; right: 0; top: 0; width: 150px; height: 330px;
    background: linear-gradient(180deg, var(--grey-soft), rgba(230,231,232,0)); }

  /* Business cards */
  .card { width: 250px; height: 152px; }
  .card--front { left: 640px; top: 50px; padding: 22px 20px 0 70px; }
  .card--front .brand__name { font-size: 17px; }
  .card--front .tagline { font-size: 9.5px; margin: 1px 0 12px; }
  .card--front .contact { color: var(--teal); font-size: 8px; }
  .card--front .contact + .contact { margin-top: 10px; }
  .card--back { left: 910px; top: 50px; background: var(--teal);
    display: flex; flex-direction: column; align-items: center; justify-content: center; }
  .card--back .brand__mark { border-color: var(--paper); width: 24px; height: 24px; }
  .card--back .brand__name { color: var(--paper); font-size: 17px; }
  .card--back .tagline, .card--back .tagline .and { color: var(--paper); font-size: 9.5px; margin-top: 2px; }

  /* Appointment card */
  .appointment { top: 228px; width: 250px; height: 176px; }
  .appointment--cover { left: 640px; background: var(--teal); padding: 24px 20px 0 70px; color: var(--paper); }
  .appointment--cover .brand__name { color: var(--paper); font-size: 17px; }
  .appointment--cover .tagline, .appointment--cover .tagline .and { color: var(--paper); font-size: 9.5px; margin: 1px 0 12px; }
  .appointment--cover .contact { color: var(--paper); font-size: 8px; }
  .appointment--cover .contact + .contact { margin-top: 10px; }
  .appointment--inside { left: 910px; padding: 26px 20px; }
  .appt-row { display: flex; gap: 10px; margin-bottom: 20px; }
  .appt-field { flex: 1; display: flex; align-items: flex-end; gap: 6px; font-size: 9px; color: var(--teal); }
  .appt-field::after { content: ""; flex: 1; border-bottom: 1px solid var(--teal); margin-bottom: 2px; }

  /* With compliments slip */
  .compliments { left: 640px; top: 440px; width: 520px; height: 246px; }
  .compliments__brand { position: absolute; left: 30px; bottom: 32px; }
  .compliments__brand .brand__name { font-size: 21px; }
  .compliments__brand .tagline { font-size: 11.5px; margin: 2px 0 0 40px; }
  .compliments__band { position: absolute; right: 28px; top: 0; width: 140px; height: 200px;
    background: var(--teal-light); padding: 0 12px 14px; display: flex; flex-direction: column; justify-content: flex-end; }
  .compliments__band .contact { color: var(--paper); font-size: 7.5px; }
  .compliments__band .contact + .contact { margin-top: 8px; }
  .compliments__title { position: absolute; right: 28px; bottom: 16px; width: 140px; text-align: center;
    color: var(--teal); font-size: 16px; }
</style>
</head>
<body>

  <section class="sheet letterhead">
    <div class="letterhead__pattern" role="img" aria-label="Faint grey overlapping circle pattern decoration"></div>
    <header class="letterhead__header">
      <div class="brand"><span class="brand__mark"></span><span class="brand__name">Dr Clara Westwood</span></div>
      <span class="letterhead__divider"></span>
      <span class="tagline">Obstetrician <span class="and">and</span> Gynaecologist</span>
    </header>
    <div class="letterhead__contact">
      <p class="contact">Harbourside Private Hospital<br>Suite 4 Spec. Med. Centre (West)<br>Marlowe Ave, Harbourside<br>Tel: 9100 2300 Fax: 9100 2301</p>
      <p class="contact">web: drclarawestwood.com.au<br>email: clara@drclarawestwood.com.au</p>
    </div>
  </section>

  <section class="sheet card card--front">
    <div class="brand__name">Dr Clara Westwood</div>
    <div class="tagline">Obstetrician <span class="and">and</span> Gynaecologist</div>
    <p class="contact">Harbourside Private Hospital<br>Suite 4 Spec. Med. Centre (West)<br>Marlowe Ave, Harbourside<br>Tel: 9100 2300 Fax: 9100 2301</p>
    <p class="contact">web: drclarawestwood.com.au<br>email: clara@drclarawestwood.com.au</p>
  </section>

  <section class="sheet card card--back">
    <div class="brand"><span class="brand__mark"></span><span class="brand__name">Dr Clara Westwood</span></div>
    <div class="tagline">Obstetrician <span class="and">and</span> Gynaecologist</div>
  </section>

  <section class="sheet appointment appointment--cover">
    <div class="brand__name">Dr Clara Westwood</div>
    <div class="tagline">Obstetrician <span class="and">and</span> Gynaecologist</div>
    <p class="contact">Harbourside Private Hospital<br>Suite 4 Spec. Med. Centre (West)<br>Marlowe Ave, Harbourside<br>Tel: 9100 2300 Fax: 9100 2301</p>
    <p class="contact">web: drclarawestwood.com.au<br>email: clara@drclarawestwood.com.au</p>
  </section>

  <section class="sheet appointment appointment--inside">
    <div class="appt-row"><span class="appt-field">Name</span></div>
    <div class="appt-row"><span class="appt-field">Date</span><span class="appt-field">Time</span></div>
    <div class="appt-row"><span class="appt-field">Date</span><span class="appt-field">Time</span></div>
    <div class="appt-row"><span class="appt-field">Date</span><span class="appt-field">Time</span></div>
  </section>

  <section class="sheet compliments">
    <div class="compliments__brand">
      <div class="brand"><span class="brand__mark"></span><span class="brand__name">Dr Clara Westwood</span></div>
      <div class="tagline">Obstetrician <span class="and">and</span> Gynaecologist</div>
    </div>
    <div class="compliments__band">
      <p class="contact">Harbourside Private Hospital<br>Suite 4 Spec. Med. Centre (West)<br>Marlowe Ave, Harbourside<br>Tel: 9100 2300 Fax: 9100 2301</p>
      <p class="contact">web: drclarawestwood.com.au<br>email: clara@drclarawestwood.com.au</p>
    </div>
    <div class="compliments__title">With Compliments</div>
  </section>

</body>
</html>
```